Presentation Folder Design for a growing Physical Therapy Network.

This standard two-sided folder will be used when making sales and other presentations. It must represent the company positively and include:
The company logo (already created by ArtHive), one or more photographs that represent either/ or:
Physical Therapists working with injured workers
Injured workers

Meridian Recovery Alliance is the company and it cares for injured workers. We don't want people who look like they are in pain but more upbeat and happy workers or patients. Industries we serve include teachers, bus drivers, construction, healthcare, city workers, etc. We have an account with PixVaultImages if stock photos are best. A front and back for the folder is preferred, although it could simply be a continuation. I can provide the company logo(s) to any interested party.

I went in under "book cover", although this is NOT a book cover but it seemed the best fit from the categories I could select.
Updates

                                      Based on inquiries, I wanted to provide an update.  The size of the folder is 9" wide by 12" high.  I am attempting to attach a logo using the ArtHive messaging 'paste' function but I don't think it is working so if you send me your email, I will promptly forward it to you. (alternatively, if someone could tell me how to do it?).  Do not use the one from our website as it has changed.  Our new website will launch later this month.  Regarding guaranteeing payment.  I have not triggered it yet as I am having some bad luck on another project where the designers clearly did not read my instructions and I guaranteed payment.  It may still work out but I have a ways to go.  I am hopeful that this is a simpler project.  I intend to use a design but have not yet felt confident to guarantee it this time.  No one else is working on it on our behalf.                                   

One more item...the link where it asks if I want to upload a file isn't doing anything when I click, "Add" or I would have added the logo there.  I submitted an inquiry to ArtHive about it...

Target Market(s)

Employers, healthcare providers, physicians, case managers, etc. Used to make sales presentations

Industry/Entity Type

Construction

Requirements
Must have
• As above...logo, pictures of workers...happy, attractive, etc. We are updating our website and using a fireman and a construction worker.

```html
<!DOCTYPE html>
<html lang="en">
<head>
<meta charset="utf-8">
<title>Meridian Recovery Alliance – Presentation Folder</title>
<link href="https://fonts.googleapis.com/css2?family=Roboto:wght@400;500;700&display=swap" rel="stylesheet">
<style>
  :root {
    --purple: #5b2a86;
    --charcoal: #2d2d2f;
    --ink: #3a3a3c;
    --white: #ffffff;
    --panel: #f4f4f5;
  }
  * { margin: 0; padding: 0; box-sizing: border-box; }
  html, body { width: 1200px; height: 781px; overflow: hidden; background: var(--white); }
  body { font-family: "Roboto", Arial, sans-serif; position: relative; }

  .folder {
    position: absolute; left: 67px; top: 29px; width: 1080px; height: 723px;
    background: var(--panel);
    box-shadow: 0 2px 8px rgba(0,0,0,.25);
    overflow: hidden;
  }
  .panel { position: absolute; }
  .panel--light { background: linear-gradient(160deg, #ffffff 0%, #eeeef0 100%); }
  .panel--dark { background: var(--charcoal); }

  .purple-band {
    position: absolute; left: 0; top: 291px; width: 1080px; height: 149px;
    background: var(--purple);
    color: var(--white);
  }
  .web-address {
    position: absolute; left: 77px; top: 62px;
    font-size: 19px; letter-spacing: 1.6px; font-weight: 400;
  }
  .band-name {
    position: absolute; right: 40px; top: 40px; text-align: right;
    font-size: 28px; font-weight: 700;
  }
  .band-tagline {
    position: absolute; right: 40px; top: 80px; text-align: right;
    font-size: 24px; font-weight: 400;
  }

  .contact {
    position: absolute; left: 325px; top: 30px; width: 220px;
    color: var(--white); text-align: center; font-size: 10.5px; line-height: 1.35; font-weight: 700;
    font-style: normal;
  }
  .contact p { margin-bottom: 14px; }
  .contact .label { display: block; }

  .photo { position: absolute; border: 3px solid var(--white); }
  .photo--team-cutout { border: none; border-radius: 6px; }

  .brand { position: absolute; font-weight: 700; color: var(--ink); }
  .brand-mark {
    display: inline-block; width: 22px; height: 22px; background: var(--purple);
    vertical-align: top; margin-right: 10px; margin-top: 6px;
  }
  .brand-name { display: inline-block; vertical-align: top; font-size: 30px; line-height: 1.08; }
  .brand--back .brand-name { font-size: 28px; }
  .brand-tag { font-size: 14px; font-weight: 700; color: var(--purple); margin-left: 32px; }
  .brand-tag--top { margin-bottom: 6px; }
  .brand-tag--bottom { margin-top: 8px; }

  .specialty {
    position: absolute; left: 770px; top: 532px; width: 290px; text-align: center;
    font-size: 19px; line-height: 1.3; color: var(--ink);
  }
</style>
</head>
<body>
<div class="folder">
  <div class="panel panel--light" style="left:0;top:0;width:325px;height:291px;"></div>
  <div class="panel panel--dark" style="left:325px;top:0;width:427px;height:291px;"></div>
  <div class="panel panel--light" style="left:752px;top:0;width:328px;height:291px;"></div>
  <div class="panel panel--light" style="left:0;top:440px;width:325px;height:283px;"></div>
  <div class="panel panel--dark" style="left:325px;top:440px;width:427px;height:283px;"></div>
  <div class="panel panel--light" style="left:752px;top:440px;width:328px;height:283px;"></div>

  <div class="photo photo--team-cutout" role="img" aria-label="Group of smiling workers from many trades: chef, nurse, mechanic, construction worker and delivery staff" style="left:45px;top:67px;width:264px;height:200px;background:linear-gradient(180deg,#ece9ee 0%,#c7bcb4 45%,#8e8f9a 100%);"></div>

  <address class="contact">
    <p>Meridian Recovery Alliance<br>4180 W. Larkspur Avenue, Suite 200<br>Cedar Mesa, AZ 85099</p>
    <p><span class="label">Telephone:</span>+1 555 014 2270</p>
    <p><span class="label">FAX:</span>+1 555 014 2271</p>
    <p><span class="label">Toll Free:</span>+1 800 555 0199</p>
    <p><span class="label">Email:</span>info@meridianrecoveryalliance.com</p>
  </address>

  <div class="photo" role="img" aria-label="Smiling healthcare team in scrubs" style="left:549px;top:27px;width:197px;height:110px;background:linear-gradient(135deg,#dfe6ea 0%,#6fa6c8 55%,#3d6f96 100%);"></div>
  <div class="photo" role="img" aria-label="Smiling warehouse worker holding a clipboard" style="left:549px;top:161px;width:197px;height:111px;background:linear-gradient(135deg,#7a8fa3 0%,#c4a47a 50%,#4f5d6b 100%);"></div>

  <div class="brand" style="left:800px;top:90px;">
    <span class="brand-mark"></span><span class="brand-name">Meridian<br>Recovery<br>Alliance</span>
  </div>

  <div class="purple-band">
    <div class="web-address">www.meridianrecoveryalliance.com</div>
    <div class="band-name">Meridian Recovery Alliance</div>
    <div class="band-tagline">Delivering Results. Creating Savings.</div>
  </div>

  <div class="brand brand--back" style="left:60px;top:512px;">
    <div class="brand-tag brand-tag--top">Creating Savings.</div>
    <span class="brand-mark"></span><span class="brand-name">Meridian<br>Recovery<br>Alliance</span>
    <div class="brand-tag brand-tag--bottom">Delivering Results.</div>
  </div>

  <div class="photo" role="img" aria-label="Smiling construction crew in hard hats and safety vests" style="left:549px;top:461px;width:197px;height:112px;background:linear-gradient(135deg,#9fb4c6 0%,#d9833a 45%,#c9c94a 70%,#4a4f58 100%);"></div>
  <div class="photo" role="img" aria-label="Smiling firefighters in turnout gear beside a fire engine" style="left:549px;top:597px;width:197px;height:112px;background:linear-gradient(135deg,#3a2f2c 0%,#9a2e22 50%,#d8b24a 100%);"></div>

  <p class="specialty">Specializing in Industrial Injury Prevention and Rehabilitation</p>
</div>
</body>
</html>
```